KBRF website design

We need a page template website design for a cms website. Please see the brief attached for the details.
The client is the Kestrel Brook Ramfold Federation which is an organisation promoting the White Suffolk Sheep Breed within Australia.
Updates

Reason: So that my top few designs can make changes and re-submit.

Target Market(s)

See attached brief

```html
<!DOCTYPE html>
<html lang="en">
<head>
<meta charset="utf-8">
<title>Kestrel Brook Ramfold Federation</title>
<link href="https://fonts.googleapis.com/css2?family=Arimo:ital,wght@0,400;0,700;1,400&family=Rubik:wght@700&display=swap" rel="stylesheet">
<style>
:root{
  --green:#145c3d;
  --yellow:#ecd033;
  --drop:#e6c93a;
  --red:#b0122a;
  --text:#222;
  --footer:#232323;
  --footer-text:#c8c8c8;
  --social:#2d4a8a;
}
*{margin:0;padding:0;box-sizing:border-box}
html,body{width:1200px;height:1182px;overflow:hidden;background:#fff;font-family:"Arimo",Arial,sans-serif;color:var(--text)}
.page{position:relative;width:1200px;height:1182px}
.brand-mark{position:absolute;left:104px;top:24px;width:100px;height:104px;border-radius:50%;background:var(--yellow)}
.brand-name{position:absolute;left:228px;top:56px;font-family:"Rubik",Arial,sans-serif;font-weight:700;font-size:31px;color:var(--green);letter-spacing:.2px;white-space:nowrap}
.tagline{position:absolute;left:229px;top:99px;font-size:19px;color:var(--red)}
.social{position:absolute;left:936px;top:50px;width:165px;height:52px;border:2px solid var(--social);border-radius:3px;display:flex;align-items:center;padding-left:14px;color:var(--social);font-weight:700;font-size:15px}
.nav{position:absolute;left:0;top:148px;width:1200px;height:50px;background:var(--green)}
.nav ul{list-style:none;display:flex;position:absolute;left:101px;top:0;height:50px}
.nav li{position:relative;height:50px;display:flex;align-items:center;justify-content:center;color:#fff;font-weight:700;font-size:15px;border-right:1px solid #2a7050}
.nav li:last-child{border-right:none}
.nav li.home{padding-right:14px}
.nav li.active{color:var(--yellow);padding-right:14px}
.nav li.active::after{content:"";position:absolute;bottom:0;left:29px;border:6px solid transparent;border-bottom-color:var(--drop);border-top:0}
.dropdown{position:absolute;left:182px;top:199px;width:163px;height:78px;background:var(--drop);padding:9px 6px 6px;z-index:2}
.dropdown div{height:28px;line-height:28px;padding-left:16px;font-size:15px;color:#222}
.dropdown .on{margin-top:6px;background:var(--green);color:#fff}
.hero{position:absolute;left:101px;top:203px;width:1000px;height:363px;background:linear-gradient(180deg,#8b8e96 0%,#a79c83 30%,#c9b68a 62%,#b8521f 80%,#c4622c 100%)}
.welcome{position:absolute;left:101px;top:592px;width:680px}
h1,h2{font-weight:700;color:var(--green);font-size:26px}
.welcome .lead{font-weight:700;font-size:16.5px;line-height:22px;margin:12px 0 10px;color:#222}
.welcome p{font-size:13.5px;line-height:20px}
.welcome p.body+p.body{margin-top:17px;line-height:19.5px}
.welcome a{color:var(--green)}
.sponsors{position:absolute;left:824px;top:593px;width:277px}
.ad{margin-top:16px;width:274px;height:213px;background:var(--yellow);position:relative}
.ad-title{padding:9px 0 0 12px;color:var(--green);font-size:16px;line-height:22px}
.ad-title b{font-size:20px}
.ad-photo{position:absolute;left:0;top:57px;width:274px;height:129px;background:linear-gradient(180deg,#a9b59a,#d8d2c2 45%,#6e9a42 100%)}
.ad-url{position:absolute;left:11px;top:189px;font-weight:700;font-size:16px;color:var(--green);letter-spacing:.5px}
.tile{position:absolute;top:901px;height:131px;overflow:hidden}
.tile .cap{position:absolute;left:0;bottom:0;width:100%;background:rgba(20,20,20,.85);color:#fff;font-weight:700;font-size:14px;padding:0 12px;height:39px;display:flex;align-items:center;letter-spacing:.3px;line-height:18px}
.t1{left:101px;width:224px;background:linear-gradient(135deg,#b4a88c,#4b7bb9)}
.t2{left:358px;width:226px;background:linear-gradient(135deg,#f2f2f2,#c4c4c4)}
.t3{left:615px;width:230px;background:linear-gradient(135deg,#d8b48a,#9c7452)}
.t4{left:875px;width:226px;background:linear-gradient(135deg,#6f86a6,#dfe4ea)}
.t1 .cap{padding-left:20px}
.t4 .cap{padding-left:10px}
.footer{position:absolute;left:0;top:1089px;width:1200px;height:93px;background:var(--footer);color:var(--footer-text);font-size:14px;line-height:22px}
.footer .left{position:absolute;left:118px;top:25px}
.footer .right{position:absolute;left:839px;top:26px;font-size:13.5px}
.footer a{color:var(--footer-text)}
.sep{margin:0 10px}
</style>
</head>
<body>
<div class="page">
  <header>
    <div class="brand-mark"></div>
    <div class="brand-name">Kestrel Brook Ramfold Federation</div>
    <div class="tagline">Raised on Open Country</div>
    <div class="social">Find us on Flockbook</div>
  </header>

  <nav class="nav">
    <ul>
      <li class="home" style="width:73px">Home</li>
      <li class="active" style="width:100px">About</li>
      <li style="width:102px">Search</li>
      <li style="width:178px">Member Services</li>
      <li style="width:84px">Stud</li>
      <li style="width:100px">Pages</li>
      <li style="width:92px">News</li>
      <li style="width:89px">Sales</li>
      <li style="width:95px">Links</li>
      <li style="width:102px">Contact</li>
    </ul>
  </nav>
  <div class="dropdown">
    <div>Breed</div>
    <div class="on">Genetic Testing</div>
  </div>

  <div class="hero" role="img" aria-label="Photo of a row of white sheep standing on red earth before a hillside"></div>

  <section class="welcome">
    <h1>Welcome to KBRF</h1>
    <p class="lead">Lorem Ipsum is simply dummy of the printing and typesetting industry.</p>
    <p class="body">Contrary to popular belief, Lorem Ipsum is not <a href="#">simply random text</a>. It has roots in a piece of classical Latin literature from 45 BC, making it over 2000 years old. Harold Penwarden, a Latin professor text of the printing and typesetting industry. Lorem Ipsum has been the industry's standard dummy text ever since the 1500s, when an unknown text of the printing and typesetting industry. Lorem Ipsum has been the industry's standard dummy text ever since the 1500s.</p>
    <p class="body">when an unknown printer took a galley of type and scrambled it to <a href="#">make a type specimen</a> book. It has survived not only five centuries, but also the leap into electronic typesetting, remaining unchanged text of the printing and typesetting industry.</p>
  </section>

  <aside class="sponsors">
    <h2>Sponsors</h2>
    <div class="ad">
      <div class="ad-title">Kestrel Brook<br><b>Ramfold Federation</b></div>
      <div class="ad-photo" role="img" aria-label="Photo of a flock of sheep on green pasture"></div>
      <div class="ad-url">www.kbrf-flock.org</div>
    </div>
  </aside>

  <a class="tile t1" role="img" aria-label="Photo of a breeder holding a ribbon beside sheep"><span class="cap">Prime Lamb Helpline</span></a>
  <a class="tile t2" role="img" aria-label="Photo of a calendar with pins"><span class="cap">Events</span></a>
  <a class="tile t3" role="img" aria-label="Photo of joined hands in a circle"><span class="cap">Members Resources &amp;<br>WebManager Login</span></a>
  <a class="tile t4" role="img" aria-label="Photo of a folded newspaper on a keyboard"><span class="cap">Latest News</span></a>

  <footer class="footer">
    <div class="left">Address: PO Box 417, Fernhill, SA 5190<br>Phone :08 8400 61725<span class="sep">|</span>Fax: 08 8400 6190<span class="sep">|</span>Email office@kbrf-mail.org</div>
    <div class="right">Copyright Kestrel Brook Ramfold Federation<br>Website design and development by <a href="#">Larchpoint</a></div>
  </footer>
</div>
</body>
</html>
```